Beacon Lending and Capital. We provide MOSTLY residential home mortgages in Florida AND commercial loans for investment properties throughout the United states.
I would love to emulate so of the lender sites that are available on the internet but I would like to have the site as popular as possible for SEO purposes. Clients can already click the link to take them to the mortgage application where they can complete that and upload documents. If you could polish that up for me that would be great. I can also provide you with great detail on loan programs that are currently being offered. WE OFFER ALL MORTGAGE LENDING PRODUCTS. I would also like to add something in reference to the rate but I don't think it's legal to actually state or promise a rate for mortgage since they vary based on loan type, client and other criteria...

On the Beacon real estate site I would like to add a link or some way for clients to be able to put in credit card information to render services ...

Please let me know what you need from me

Thank you !!

Current link to site to improve and code

https://beaconlendingandcapital.example/

Industry/Entity Type

Residential and commmercial lending

Coding

Coded - Design and coding required

Number of Pages Required

2 page

Requirements
Must have
• Love to integrate Mortgage interest rates even if general
Nice to have
• Link to fill out mortgage application via Quillo MLO software

```html
<!DOCTYPE html>
<html lang="en">
<head>
<meta charset="utf-8">
<title>Beacon Lending and Capital — Business &amp; Commercial Division</title>
<link href="https://fonts.googleapis.com/css2?family=Montserrat:wght@600;700;800&family=Poppins:wght@400;500&display=swap" rel="stylesheet">
<style>
:root{
  --green-dark:#1e3b1f;
  --green-deep:#24432a;
  --lime:#8db32b;
  --lime-text:#8db32b;
  --ink:#1b1b1b;
  --body:#4a4a4a;
  --paper:#f7f6f3;
  --mist:#dfe3de;
  --white:#ffffff;
}
*{box-sizing:border-box;margin:0;padding:0}
html,body{width:1200px;height:3483px;overflow:hidden}
body{position:relative;background:var(--paper);font-family:"Poppins",sans-serif;color:var(--ink)}
.abs{position:absolute}
.heading{font-family:"Montserrat",sans-serif;font-weight:800;text-transform:uppercase;letter-spacing:.5px}
.btn{position:absolute;display:flex;align-items:center;justify-content:center;text-align:center;background:var(--lime);color:var(--white);border-radius:30px;font-family:"Montserrat",sans-serif;font-weight:600;font-size:17px;text-transform:uppercase;text-decoration:none;line-height:1.4}

/* header */
.site-header{position:absolute;left:0;top:0;width:1200px;height:108px;background:var(--white)}
.brand{position:absolute;display:flex;align-items:center;gap:12px}
.brand-dot{border-radius:50%;background:var(--green-dark)}
.brand-name{font-family:"Montserrat",sans-serif;font-weight:700;color:var(--green-dark);text-transform:uppercase}
.brand-sub{font-family:"Montserrat",sans-serif;font-weight:600;color:var(--green-dark);text-transform:uppercase}
.nav a{position:absolute;top:42px;font-family:"Poppins",sans-serif;font-size:17px;color:var(--ink);text-decoration:none;text-transform:uppercase}
.nav a.active{color:var(--lime-text)}

/* hero */
.hero{position:absolute;left:0;top:108px;width:1200px;height:589px;
  background:linear-gradient(90deg,rgba(30,59,31,.85) 0%,rgba(30,59,31,.35) 45%,rgba(30,59,31,0) 70%),
  linear-gradient(160deg,#8a9a86 0%,#5f7f4e 35%,#4c8a36 60%,#7e8c80 100%)}
.hero h1{position:absolute;left:108px;top:122px;font-size:52px;line-height:60px;color:var(--white)}
.hero p{position:absolute;left:109px;top:324px;width:420px;font-size:17.5px;line-height:28px;color:var(--white)}

/* about */
.about{position:absolute;left:0;top:697px;width:1200px;height:687px;background:var(--paper)}
.photo{position:absolute}
.badge{position:absolute;left:447px;top:76px;width:105px;height:90px;background:var(--paper)}
.badge span{position:absolute;left:6px;top:6px;width:93px;height:78px;background:var(--green-dark);color:var(--white);font-family:"Montserrat",sans-serif;font-weight:600;font-size:18px;display:flex;align-items:center;justify-content:center;text-align:center;line-height:26px}
.about h2{position:absolute;left:612px;top:98px;font-size:40px;line-height:48px;color:var(--ink)}
.about p{position:absolute;left:612px;top:268px;width:490px;font-size:16.5px;line-height:28.3px;color:var(--body)}
.deco-circle{position:absolute;border-radius:50%;background:#ecebe7}

/* properties */
.properties{position:absolute;left:0;top:1384px;width:1200px;height:699px;background:linear-gradient(180deg,var(--mist) 0%,var(--paper) 80%)}
.properties h2{position:absolute;left:0;top:88px;width:1200px;text-align:center;font-size:40px;color:var(--ink)}
.card{position:absolute;top:181px;width:313px;height:419px;overflow:hidden}
.card .label{position:absolute;left:0;bottom:22px;width:100%;text-align:center;font-family:"Montserrat",sans-serif;font-weight:600;font-size:22px;color:var(--white)}
.arrow{position:absolute;top:367px;width:48px;height:48px;border-radius:50%;background:var(--white);display:flex;align-items:center;justify-content:center;box-shadow:0 2px 8px rgba(0,0,0,.08)}

/* rates */
.rates{position:absolute;left:0;top:2083px;width:1200px;height:463px;background:linear-gradient(90deg,#1f3d22 0%,#284a2c 60%,#2d5032 100%)}
.rates h2{position:absolute;left:110px;top:76px;font-size:40px;line-height:48px;color:var(--white)}
.rates p{position:absolute;left:109px;top:199px;width:490px;font-size:16.5px;line-height:28.3px;color:var(--white)}
.rate-ring{position:absolute;left:656px;top:34px;width:392px;height:392px;border-radius:50%;background:#4e6a4f}
.rate-disc{position:absolute;left:14px;top:14px;width:364px;height:364px;border-radius:50%;background:var(--white);text-align:center}
.rate-title{position:absolute;left:0;top:94px;width:100%;font-family:"Montserrat",sans-serif;font-weight:600;font-size:22px;line-height:29px;color:var(--ink)}
.rate-line{position:absolute;left:0;width:100%;display:flex;justify-content:center;align-items:baseline;gap:8px}
.rate-line b{font-family:"Montserrat",sans-serif;font-weight:800;font-size:44px;color:var(--ink)}
.rate-line small{font-size:16px;color:var(--ink);width:44px;text-align:left}

/* contact */
.contact{position:absolute;left:0;top:2546px;width:1200px;height:694px;background:var(--paper)}
.contact h2{position:absolute;left:0;top:92px;width:1200px;text-align:center;font-size:40px;color:var(--ink)}
.contact .lede{position:absolute;left:0;top:163px;width:1200px;text-align:center;font-size:16.5px;color:var(--body)}
.field{position:absolute;background:var(--white);font-size:16.5px;color:var(--body);padding:17px 19px;line-height:22px}

/* footer */
.site-footer{position:absolute;left:0;top:3240px;width:1200px;height:243px;background:var(--white)}
.foot-links a{position:absolute;top:87px;font-size:16.5px;color:var(--body);text-decoration:none}
.copy{position:absolute;left:574px;top:125px;font-size:16.5px;color:var(--body)}
.social{position:absolute;top:86px;width:44px;height:44px;border-radius:50%;border:1.5px solid var(--green-dark);display:flex;align-items:center;justify-content:center}
.social i{display:block;width:12px;height:12px;border-radius:50%;background:var(--lime)}
</style>
</head>
<body>

<header class="site-header">
  <div class="brand" style="left:110px;top:14px">
    <div class="brand-dot" style="width:74px;height:74px"></div>
    <div>
      <div class="brand-name" style="font-size:7.5px;letter-spacing:.2px">Beacon Lending and Capital of Florida</div>
      <div class="brand-sub" style="font-size:5.5px;letter-spacing:2.2px;margin-top:4px">Business and Commercial Division</div>
    </div>
  </div>
  <nav class="nav">
    <a href="#" class="active" style="left:588px">Home</a>
    <a href="#" style="left:682px">About</a>
    <a href="#" style="left:784px">Properties</a>
  </nav>
  <a href="#" class="btn" style="left:935px;top:27px;width:154px;height:53px">Contact Us</a>
</header>

<section class="hero" role="img" aria-label="Aerial photograph of a green residential neighbourhood beside a golf course">
  <h1 class="heading">Business &amp;<br>Commercial<br>Division</h1>
  <p>Residential home mortgages in Florida and commercial loans for investment properties throughout the United states</p>
  <a href="#" class="btn" style="left:110px;top:447px;width:350px;height:62px;font-size:16px;font-weight:500;font-family:'Poppins',sans-serif">Fill out mortgage application<br>to begin lending pr</a>
</section>

<section class="about">
  <div class="deco-circle" style="left:985px;top:60px;width:210px;height:210px"></div>
  <div class="photo" role="img" aria-label="Modern timber and black clad home with a large tree and lawn" style="left:111px;top:108px;width:425px;height:475px;background:linear-gradient(180deg,#c9dbe8 0%,#8a9a7a 35%,#6b5a45 60%,#5f9a3a 80%,#4f8a2e 100%)"></div>
  <div class="badge"><span>ABOUT<br>US</span></div>
  <h2 class="heading">Welcome to<br>Beacon Lending<br>and Capital</h2>
  <p>Beacon Lending Originates Residential Home loans in Florida and Commercial and business financing in all 50 States. We have over 25 years of experience in ALL types of real estate and commercial lending. We are strategically partnered to help you obtain ALL necessary components of residential and commercial lending. From the RIGHT lending partners to the best practice Insurance avenues and commercial and residential real estate partners</p>
  <a href="#" class="btn" style="left:613px;top:526px;width:153px;height:54px">Contact Us</a>
</section>

<section class="properties">
  <h2 class="heading">Available Properties</h2>
  <div class="arrow" style="left:64px"><svg width="14" height="14" viewBox="0 0 14 14"><path d="M9 2 4 7l5 5" fill="none" stroke="#1b1b1b" stroke-width="1.8"/></svg></div>
  <div class="card" role="img" aria-label="White clad modern townhouse with balcony" style="left:111px;background:linear-gradient(180deg,#dfe1e3 0%,#cfd1d2 45%,#8a7b6a 75%,#3f3f40 100%)"><div class="label">18 Harbor Lane</div></div>
  <div class="card" role="img" aria-label="Dark modern house lit at dusk among trees" style="left:444px;background:linear-gradient(180deg,#6f7f85 0%,#2b3a44 40%,#1f262b 70%,#7a4a25 100%)"><div class="label">27 Cedar Avenue</div></div>
  <div class="card" role="img" aria-label="Modern building with red timber slats and blue sky" style="left:776px;background:linear-gradient(90deg,#8a4d3d 0%,#9a5a47 45%,#bfc6cb 65%,#6f9fd0 100%)"><div class="label">64 Maple Court</div></div>
  <div class="arrow" style="left:1089px"><svg width="14" height="14" viewBox="0 0 14 14"><path d="M5 2l5 5-5 5" fill="none" stroke="#1b1b1b" stroke-width="1.8"/></svg></div>
</section>

<section class="rates" role="region" aria-label="Today's mortgage rates over a city skyline backdrop">
  <h2 class="heading">Today’s<br>Mortgage Rates</h2>
  <p>Duis aute irure dolor in reprehenderit in voluptate velit esse cillum dolore eu fugiat nulla pariatur. Excepteur sint occaec cupidatat noproident.</p>
  <a href="#" class="btn" style="left:110px;top:322px;width:264px;height:53px">See Refinance Rates</a>
  <div class="rate-ring">
    <div class="rate-disc">
      <div class="rate-title">Today’s 30-year fixed<br>mortgage rates</div>
      <div class="rate-line" style="top:180px"><b>6.875%</b><small>Rate</small></div>
      <div class="rate-line" style="top:234px"><b>7.038%</b><small>APR 1</small></div>
    </div>
  </div>
</section>

<section class="contact">
  <h2 class="heading">Get in Touch</h2>
  <p class="lede">Please send me a message for general inquiries or reservations.</p>
  <div class="field" style="left:162px;top:232px;width:430px;height:55px">First Name*</div>
  <div class="field" style="left:609px;top:232px;width:430px;height:55px">Last Name*</div>
  <div class="field" style="left:162px;top:305px;width:430px;height:55px">Email Address*</div>
  <div class="field" style="left:609px;top:305px;width:430px;height:55px">Phone Number*</div>
  <div class="field" style="left:162px;top:377px;width:877px;height:125px">Message</div>
  <a href="#" class="btn" style="left:537px;top:551px;width:126px;height:53px">Send</a>
  <div class="deco-circle" style="left:1060px;top:560px;width:130px;height:130px"></div>
</section>

<footer class="site-footer">
  <div class="brand" style="left:110px;top:46px">
    <div class="brand-dot" style="width:104px;height:104px"></div>
    <div>
      <div class="brand-name" style="font-size:8.5px;letter-spacing:.3px">Beacon Lending and Capital of Florida</div>
      <div class="brand-sub" style="font-size:6.5px;letter-spacing:2.6px;margin-top:5px">Business and Commercial Division</div>
    </div>
  </div>
  <nav class="foot-links">
    <a href="#" style="left:574px">Home</a>
    <a href="#" style="left:657px">About</a>
    <a href="#" style="left:741px">Properties</a>
  </nav>
  <p class="copy">© 2025. All Rights Reserved.</p>
  <a href="#" class="social" style="left:941px" aria-label="Social profile"><i></i></a>
  <a href="#" class="social" style="left:992px" aria-label="Social profile"><i></i></a>
  <a href="#" class="social" style="left:1044px" aria-label="Social profile"><i></i></a>
</footer>

</body>
</html>
```